web site update

I want to get a better website for a small high end remodeling and construction company
I currently have a web site but you will find that it is not good.
www.quenbrickhall.com
We are a high end construction / remodeling company that has been in business since 2003. We primarily work in the mid peninsula of the bay area. Most of our clientele are very educated captains of industry. This group is still the target client.
I had my logo designed by Mint Easel a few years ago and I do like it, I like the orange and black or orange a blue. I don’t have a lot of content on hand as far as professional photographs.
Number of pages not sure and are open to: design pages vs full function website
I think what I am after is a web presence that will seal the deal as we are getting high referrals from past clients.
Construction
1 page

```html
<!DOCTYPE html>
<html lang="en">
<head>
<meta charset="utf-8">
<title>Quenbrick Hall Remodeling</title>
<link rel="stylesheet" href="https://fonts.googleapis.com/css2?family=Raleway:wght@400;500;600;700;800&display=swap">
<style>
:root{
  --orange:#f26a10;
  --orange-deep:#e05a06;
  --ink:#1e1e1e;
  --text:#333333;
  --muted:#8a8a8a;
  --line:#f5b183;
  --band:#333333;
  --night:#1b1b1b;
  --card:#3b3b3b;
  --white:#ffffff;
}
*{margin:0;padding:0;box-sizing:border-box}
html,body{width:1200px;height:2579px;overflow:hidden;background:var(--white)}
body{position:relative;font-family:"Raleway",sans-serif;color:var(--text)}
.abs{position:absolute}
.brand{display:flex;align-items:center;gap:12px}
.brand-mark{width:40px;height:40px;background:var(--ink)}
.brand-name{font-weight:800;font-size:21px;line-height:1.05;color:var(--orange);text-transform:uppercase;letter-spacing:1px}
.phone-btn{left:853px;top:34px;width:156px;height:34px;background:var(--orange);color:var(--white);display:flex;align-items:center;gap:10px;padding-left:8px;font-size:12px}
.phone-btn .sep{width:1px;height:22px;background:rgba(255,255,255,.7)}
.main-nav{left:0;top:103px;width:1200px;height:40px;border-top:1px solid var(--line);border-bottom:1px solid var(--line)}
.main-nav a{position:absolute;top:11px;font-size:13px;color:var(--ink);text-decoration:none}
.main-nav a.active{color:var(--orange)}
.search{left:853px;top:7px;width:156px;height:26px;border:1px solid var(--line)}
.search span{position:absolute;left:8px;top:6px;font-size:9px;color:#bbb}
.search svg{position:absolute;right:0;top:0;width:26px;height:24px;border-left:1px solid var(--ink)}
.hero{left:0;top:151px;width:1200px;height:478px;background:linear-gradient(120deg,#b8916a 0%,#9c7550 40%,#7d5a3c 70%,#a9845f 100%)}
.hero-panel{left:249px;top:100px;width:397px;height:277px;background:rgba(60,50,40,.55);border:1px solid rgba(255,255,255,.35);padding:20px 34px;color:var(--white)}
.hero-panel h1{font-weight:500;font-size:27px;line-height:1.2;margin-bottom:12px}
.hero-panel p{font-size:13.5px;line-height:1.45}
.btn{display:inline-block;background:var(--orange);color:var(--white);font-size:13px;text-align:center}
.hero-panel .btn{margin-top:16px;width:119px;height:32px;line-height:32px}
.hero-arrow{top:222px;width:34px;height:34px;border:2px solid var(--white);border-radius:50%}
.sec-title{font-size:17px;font-weight:500;color:var(--orange);padding-bottom:4px;border-bottom:2px solid var(--line);display:inline-block}
.mini-arrow{width:20px;height:20px;border:1px solid #bbb;background:var(--white)}
.project{width:239px}
.project .photo{height:157px;position:relative}
.project .tag{position:absolute;left:0;bottom:0;background:var(--orange);color:var(--white);font-size:12px;font-weight:600;padding:3px 6px}
.project p{font-size:10.5px;line-height:1.45;margin-top:8px;color:var(--ink)}
.more{font-size:11px;color:var(--orange);margin-top:8px;display:block}
.event{left:718px;width:291px;height:76px}
.event .thumb{position:absolute;left:0;top:0;width:76px;height:76px}
.event h4{position:absolute;left:94px;top:2px;font-size:14px;font-weight:500;color:var(--ink)}
.event p{position:absolute;left:94px;top:22px;font-size:10px;line-height:1.45;color:var(--ink);width:197px}
.event p b{font-weight:400;color:var(--orange)}
.band{left:0;top:1002px;width:1200px;height:66px;background:var(--band)}
.band p{position:absolute;left:191px;top:22px;color:var(--orange);font-size:16.5px}
.band .outline{position:absolute;left:849px;top:12px;width:160px;height:40px;border:2px solid var(--orange);color:var(--orange);font-size:17px;text-align:center;line-height:36px}
.testimonials{left:0;top:1068px;width:1200px;height:419px;background:radial-gradient(ellipse at 50% 40%,#2c2c2c,var(--night))}
.testimonials h2{position:absolute;left:0;width:1200px;top:28px;text-align:center}
.testimonials h2 span{font-size:17px;font-weight:500;color:var(--orange);border-bottom:2px solid var(--orange);padding:0 4px 4px;border-top:1px solid var(--orange);padding-top:4px}
.t-card{left:191px;top:92px;width:239px;height:238px;background:var(--card);border:2px solid #555;text-align:center;color:var(--white)}
.t-card .avatar{position:absolute;left:49px;top:20px;width:137px;height:137px;border-radius:50%;border:4px solid var(--white);background:linear-gradient(160deg,#c9dff0,#6f9fd0)}
.t-card .name{position:absolute;top:174px;width:100%;font-size:14px}
.t-card .role{position:absolute;top:196px;width:100%;font-size:9.5px;color:#ccc}
.t-quote{left:478px;top:140px;width:528px;font-size:11.5px;line-height:24px;color:var(--white)}
.t-arrow{top:360px;width:20px;height:20px;background:var(--white)}
.post{width:239px}
.post .photo{height:150px}
.post h3{font-size:13.5px;font-weight:600;color:var(--orange);margin-top:16px}
.post .meta{font-size:9px;color:#c4c4c4;margin-top:6px}
.post p{font-size:10.5px;line-height:1.55;color:var(--ink);margin-top:6px}
.post .btn{margin-top:22px;width:119px;height:31px;line-height:31px}
.partners-rule{left:191px;width:818px;height:1px;background:var(--line)}
.badge{top:2046px}
.footer{left:0;top:2224px;width:1200px;height:320px;background:var(--orange-deep);color:var(--white)}
.footer .logo-box{position:absolute;left:191px;top:56px;width:223px;height:87px;background:var(--white);padding:0 14px;display:flex;align-items:center}
.footer h5{position:absolute;top:48px;font-size:14px;font-weight:500}
.links{position:absolute;left:600px;top:84px;list-style:none}
.links li{font-size:10px;height:19px;padding-left:16px;position:relative}
.links li::before{content:"";position:absolute;left:2px;top:3px;width:5px;height:5px;border-right:1.5px solid var(--white);border-top:1.5px solid var(--white);transform:rotate(45deg)}
.social{position:absolute;left:805px;display:flex;align-items:center;gap:14px;font-size:10px}
.social i{width:44px;height:44px;border-radius:50%;background:var(--white);display:block}
.legal{position:absolute;left:191px;top:258px;font-size:9.5px}
.copyright{left:0;top:2544px;width:1200px;height:35px;background:var(--night);color:var(--white);font-size:9.5px;text-align:center;line-height:35px}
</style>
</head>
<body>

<header>
  <div class="abs brand" style="left:191px;top:22px">
    <span class="brand-mark"></span>
    <span class="brand-name">Quenbrick Hall<br>Remodeling</span>
  </div>
  <div class="abs phone-btn">
    <svg width="22" height="22" viewBox="0 0 24 24" fill="none" stroke="#fff" stroke-width="1.8"><path d="M5 3h4l2 5-2.5 1.5a11 11 0 0 0 6 6L16 13l5 2v4a2 2 0 0 1-2 2A17 17 0 0 1 3 5a2 2 0 0 1 2-2z"/></svg>
    <span class="sep"></span>
    <span>+1-650-555-0182</span>
  </div>
</header>

<nav class="abs main-nav">
  <a class="active" href="#" style="left:215px">Home</a>
  <a href="#" style="left:301px">Projects</a>
  <a href="#" style="left:387px">Services</a>
  <a href="#" style="left:474px">Blog</a>
  <a href="#" style="left:560px">Contact</a>
  <div class="abs search"><span>Search</span>
    <svg viewBox="0 0 26 24"><circle cx="12" cy="11" r="5" fill="none" stroke="#1e1e1e" stroke-width="2"/><line x1="15.5" y1="14.5" x2="20" y2="19" stroke="#1e1e1e" stroke-width="2"/></svg>
  </div>
</nav>

<section class="abs hero" role="img" aria-label="Carpentry tools, wood samples and a hand saw laid out on a wooden workbench">
  <div class="abs hero-panel">
    <h1>The Remodeling Experts<br>of the Town</h1>
    <p>Sed ut perspiciatis unde omnis iste natus error sit voluptatem accusantium doloremque laudantium, totam rem aperiam, eaque ipsa quae ab illo inventore veritatis et quasi architecto beatae vitae dicta sunt explicabo. Nemo enim ipsam</p>
    <span class="btn">Read More</span>
  </div>
  <svg class="abs hero-arrow" style="left:172px" viewBox="0 0 34 34"><polyline points="19,10 12,17 19,24" fill="none" stroke="#fff" stroke-width="2"/></svg>
  <svg class="abs hero-arrow" style="left:989px" viewBox="0 0 34 34"><polyline points="14,10 21,17 14,24" fill="none" stroke="#fff" stroke-width="2"/></svg>
</section>

<section>
  <h2 class="abs sec-title" style="left:191px;top:659px">Current Projects</h2>
  <svg class="abs mini-arrow" style="left:641px;top:662px" viewBox="0 0 20 20"><polyline points="12,6 8,10 12,14" fill="none" stroke="#1e1e1e" stroke-width="1.6"/></svg>
  <svg class="abs mini-arrow" style="left:664px;top:662px" viewBox="0 0 20 20"><polyline points="8,6 12,10 8,14" fill="none" stroke="#1e1e1e" stroke-width="1.6"/></svg>

  <article class="abs project" style="left:191px;top:703px">
    <div class="photo" role="img" aria-label="Child with a colour swatch fan and paint cans in a white room" style="background:linear-gradient(135deg,#f4f4f6,#e2e4ea 60%,#f0c9a0)"><span class="tag">Lorem ipsum dolor sit</span></div>
    <p>exercitation ullamco laboris nisi ut aliquip ex ea commodo consequat. Duis aute irure dolor in reprehenderit in voluptate velit esse cillum dolore eu fugiat nulla pariatur. Excepteur sint occaecat cupidatat non proident,</p>
    <span class="more">More »</span>
  </article>
  <article class="abs project" style="left:447px;top:703px">
    <div class="photo" role="img" aria-label="Backyard patio with outdoor dining set beside a house" style="background:linear-gradient(180deg,#7fa35a,#5f6d63 50%,#8d8a80)"><span class="tag">Lorem ipsum dolor sit</span></div>
    <p>exercitation ullamco laboris nisi ut aliquip ex ea commodo consequat. Duis aute irure dolor in reprehenderit in voluptate velit esse cillum dolore eu fugiat nulla pariatur. Excepteur sint occaecat cupidatat non proident,</p>
    <span class="more">More »</span>
  </article>

  <h2 class="abs sec-title" style="left:718px;top:659px">Events</h2>
  <div class="abs event" style="top:703px">
    <div class="thumb" role="img" aria-label="Team reviewing plans at a desk" style="background:linear-gradient(135deg,#c9b29a,#7a6656)"></div>
    <h4>Ut enim ad minima</h4>
    <p>quia dolor sit amet, consectetur, adipisci velit, sed quia non numquam quia dolor sit amet non numquam <b>More</b></p>
  </div>
  <div class="abs event" style="top:787px">
    <div class="thumb" role="img" aria-label="Finished wooden kitchen interior" style="background:linear-gradient(135deg,#8a4d2a,#3c2416)"></div>
    <h4>Ut enim ad minima</h4>
    <p>quia dolor sit amet, consectetur, adipisci velit, sed quia non numquam quia dolor sit amet non numquam <b>More</b></p>
  </div>
  <div class="abs event" style="top:873px">
    <div class="thumb" role="img" aria-label="Drafting tools on architectural plans" style="background:linear-gradient(135deg,#e8ecef,#9aa3ab)"></div>
    <h4>Ut enim ad minima</h4>
    <p>quia dolor sit amet, consectetur, adipisci velit, sed quia non numquam quia dolor sit amet non numquam <b>More</b></p>
  </div>
</section>

<section class="abs band">
  <p>We are professionals to meet New Standards of Remodeling</p>
  <span class="outline">Contact Us</span>
</section>

<section class="abs testimonials" role="img" aria-label="Dark workbench with power tools and cables in the background">
  <h2><span>Clients Testimonial</span></h2>
  <div class="abs t-card">
    <div class="avatar" role="img" aria-label="Portrait of the client"></div>
    <div class="name">Dana Whitlow</div>
    <div class="role">Ass. Director Brightmore Inc</div>
  </div>
  <p class="abs t-quote">perspiciatis unde omnis iste natus error sit voluptatem accusantium doloremque laudantium, totam rem aperiam, eaque ipsa quae ab illo inventore veritatis et quasi architecto beatae vitae dicta sunt explicabo. Nemo enim ipsam voluptatem quia voluptas sit aspernatur aut odit aut fugit, sed quia consequuntur magni dolores eos qui ratione voluptatem sequi nesciunt. Neque porro quisquam est, qui dolorem ipsum quia dolor sit amet, consectetur, adipisci velit, sed quia non numquam eius modi tempora incidunt ut labore et dolore magnam aliquam</p>
  <svg class="abs t-arrow" style="left:578px" viewBox="0 0 20 20"><polyline points="12,6 8,10 12,14" fill="none" stroke="#1e1e1e" stroke-width="1.6"/></svg>
  <svg class="abs t-arrow" style="left:602px" viewBox="0 0 20 20"><polyline points="8,6 12,10 8,14" fill="none" stroke="#1e1e1e" stroke-width="1.6"/></svg>
</section>

<section>
  <h2 class="abs sec-title" style="left:191px;top:1541px">Blog</h2>
  <article class="abs post" style="left:191px;top:1587px">
    <div class="photo" role="img" aria-label="Hanging letter tiles on a blue background" style="background:linear-gradient(135deg,#2e9be6,#0d6fc0)"></div>
    <h3>Quis nostrud exercitation ullamco</h3>
    <div class="meta">20th May, 2015 by Owen Trask</div>
    <p>architecto beatae vitae dicta sunt explicabo. Nemo enim ipsam voluptatem quia voluptas sit aspernatur aut odit aut fugit, sed quia consequuntur magni dolores eos qui ratione voluptatem sequi nesciunt.</p>
    <span class="btn">Read More</span>
  </article>
  <article class="abs post" style="left:480px;top:1587px">
    <div class="photo" role="img" aria-label="Colourful wooden letters scattered on weathered boards" style="background:linear-gradient(135deg,#c9a57a,#8f8b84 50%,#6f8aa8)"></div>
    <h3>Quis nostrud exercitation ullamco</h3>
    <div class="meta">20th May, 2015 by Owen Trask</div>
    <p>architecto beatae vitae dicta sunt explicabo. Nemo enim ipsam voluptatem quia voluptas sit aspernatur aut odit aut fugit, sed quia consequuntur magni dolores eos qui ratione voluptatem sequi nesciunt.</p>
    <span class="btn">Read More</span>
  </article>
  <article class="abs post" style="left:770px;top:1587px">
    <div class="photo" role="img" aria-label="Woman sitting on the floor with a laptop against a white wall" style="background:linear-gradient(180deg,#f1f1f1,#e4e4e4 70%,#d9c8b4)"></div>
    <h3>Quis nostrud exercitation ullamco</h3>
    <div class="meta">20th May, 2015 by Owen Trask</div>
    <p>architecto beatae vitae dicta sunt explicabo. Nemo enim ipsam voluptatem quia voluptas sit aspernatur aut odit aut fugit, sed quia consequuntur magni dolores eos qui ratione voluptatem sequi nesciunt.</p>
    <span class="btn">Read More</span>
  </article>
</section>

<section>
  <h2 class="abs" style="left:191px;top:1981px;font-size:17px;font-weight:500;color:var(--orange)">Our Partners</h2>
  <div class="abs partners-rule" style="top:2027px"></div>
  <div class="abs badge" style="left:222px;width:76px;height:76px;border-radius:50%;background:#e8883a"></div>
  <div class="abs badge" style="left:346px;top:2060px;width:106px;height:44px;background:#d9d9d9"></div>
  <div class="abs badge" style="left:524px;top:2064px;width:155px;height:38px;background:#1e1e1e"></div>
  <div class="abs badge" style="left:712px;width:122px;height:76px;background:#eeeeee"></div>
  <div class="abs badge" style="left:892px;width:76px;height:76px;border-radius:50%;background:#9bb7a8"></div>
  <div class="abs partners-rule" style="top:2132px"></div>
</section>

<footer class="abs footer">
  <div class="logo-box brand">
    <span class="brand-mark"></span>
    <span class="brand-name">Quenbrick Hall<br>Remodeling</span>
  </div>
  <h5 style="left:600px">Quick Links</h5>
  <ul class="links">
    <li>Metal Roofing</li><li>Construction Consultant</li><li>Green Building</li>
    <li>Laminate Flooring</li><li>House Renovation</li><li>Metal Roofing</li>
    <li>Construction Consultant</li><li>Green Building</li><li>Laminate Flooring</li>
  </ul>
  <h5 style="left:805px">Follow Us</h5>
  <div class="social" style="top:83px"><i></i>Follow us on Friendline</div>
  <div class="social" style="top:138px"><i></i>Share us on Chirpwire</div>
  <div class="social" style="top:193px"><i></i>Follow us on Circlespace</div>
  <div class="legal">Site Map | Privacy Policy | Terms &amp; Conditions</div>
</footer>
<div class="abs copyright">© 2010-2015 Lindqvist Studio. All rights reserved.</div>

</body>
</html>
```